Riverstone & Pine Construction and Developments business cards

A business card with watermark background (construction work)

Company logo attached

Home improvement projects
House renovations
Bathroom and kitchen renovations
House extensions
New builds and granny flats

Director Omar Haddine
(Phone number)
omar@rpcbuildgroup.com.au
(Instagram logo) rpc_buildgroup

```html
<!DOCTYPE html>
<html lang="en">
<head>
<meta charset="utf-8">
<title>Riverstone &amp; Pine – Business Cards</title>
<link href="https://fonts.googleapis.com/css2?family=Montserrat:wght@500;700&family=Arimo:wght@400&display=swap" rel="stylesheet">
<style>
  :root {
    --page: #2a2a2b;
    --card: #0c0c0d;
    --card-edge: #1a1a1b;
    --brand-blue: #3a7fc4;
    --silver: #d6d6d6;
    --white: #f2f2f2;
    --divider: #3a3a3c;
  }
  * { margin: 0; padding: 0; box-sizing: border-box; }
  html, body { width: 1200px; height: 900px; overflow: hidden; }
  body {
    background: var(--page);
    display: flex;
    flex-direction: column;
    align-items: center;
    justify-content: center;
    gap: 56px;
    font-family: "Arimo", Arial, sans-serif;
  }
  .card {
    width: 630px;
    height: 360px;
    background: var(--card);
    border-radius: 22px;
    border: 1px solid var(--card-edge);
    box-shadow: 0 14px 30px rgba(0,0,0,.45);
    position: relative;
    color: var(--white);
  }

  /* Front */
  .card--front { display: flex; align-items: center; }
  .front__brand {
    width: 290px;
    height: 100%;
    display: flex;
    align-items: center;
    justify-content: center;
    border-right: 1px solid var(--divider);
    margin: 0;
  }
  .brand {
    display: flex;
    align-items: flex-start;
    gap: 10px;
    font-family: "Montserrat", sans-serif;
    font-weight: 700;
    line-height: 1.15;
  }
  .brand__mark { width: 14px; height: 14px; margin-top: 6px; flex: none; }
  .brand__name { font-size: 24px; }
  .brand__sub { display: block; font-size: 13px; letter-spacing: .04em; margin-top: 4px; }
  .brand--blue { color: var(--brand-blue); }
  .brand--blue .brand__mark { background: var(--brand-blue); }
  .brand--silver { color: var(--silver); }
  .brand--silver .brand__mark { background: var(--silver); }

  .front__contact { padding-left: 38px; }
  .person__name {
    font-family: "Montserrat", sans-serif;
    font-weight: 700;
    font-size: 25px;
    color: var(--brand-blue);
  }
  .person__role { font-size: 17px; margin-top: 2px; }
  .contact-list { list-style: none; margin-top: 20px; }
  .contact-list li {
    display: flex;
    align-items: center;
    gap: 10px;
    font-size: 15.5px;
    margin-bottom: 9px;
  }
  .contact-list li.social { margin-top: 16px; font-size: 17px; }
  .icon { width: 17px; height: 17px; flex: none; fill: var(--brand-blue); }
  .icon-square { width: 17px; height: 17px; background: var(--brand-blue); border-radius: 3px; flex: none; }
  .accent { color: var(--brand-blue); }

  /* Back */
  .card--back {
    display: flex;
    flex-direction: column;
    align-items: center;
    justify-content: center;
    gap: 42px;
  }
  .services { text-align: center; font-size: 16px; line-height: 1.55; }
  .services .sep { font-weight: 700; margin: 0 6px; }
</style>
</head>
<body>

<section class="card card--front">
  <div class="front__brand">
    <div class="brand brand--blue">
      <span class="brand__mark"></span>
      <span class="brand__name">Riverstone &amp; Pine<span class="brand__sub">Construction and Developments</span></span>
    </div>
  </div>
  <div class="front__contact">
    <h1 class="person__name">Omar Haddine</h1>
    <p class="person__role">Director</p>
    <ul class="contact-list">
      <li>
        <svg class="icon" viewBox="0 0 24 24" aria-hidden="true"><path d="M6.6 10.8a15 15 0 0 0 6.6 6.6l2.2-2.2a1 1 0 0 1 1-.25 11.4 11.4 0 0 0 3.6.57 1 1 0 0 1 1 1V20a1 1 0 0 1-1 1A17 17 0 0 1 3 4a1 1 0 0 1 1-1h3.5a1 1 0 0 1 1 1c0 1.25.2 2.45.57 3.6a1 1 0 0 1-.25 1z"/></svg>
        0400 555 218
      </li>
      <li>
        <svg class="icon" viewBox="0 0 24 24" aria-hidden="true"><path d="M2 5h20v14H2z" fill="none"/><path d="M2 5h20v14H2V5zm2 2v.5l8 5 8-5V7H4z"/></svg>
        omar@rpcbuildgroup.com.au
      </li>
      <li>
        <svg class="icon" viewBox="0 0 24 24" aria-hidden="true"><circle cx="12" cy="12" r="9" fill="none" stroke="#3a7fc4" stroke-width="2"/><path d="M3 12h18M12 3c3 3 3 15 0 18M12 3c-3 3-3 15 0 18" fill="none" stroke="#3a7fc4" stroke-width="1.6"/></svg>
        <span>www.<span class="accent">rpcbuildgroup</span>.com.au</span>
      </li>
      <li class="social">
        <span class="icon-square" aria-hidden="true"></span>
        rpc_buildgroup
      </li>
    </ul>
  </div>
</section>

<section class="card card--back">
  <div class="brand brand--silver">
    <span class="brand__mark"></span>
    <span class="brand__name">Riverstone &amp; Pine<span class="brand__sub">Construction and Developments</span></span>
  </div>
  <p class="services">
    Home improvement projects<span class="sep">|</span>House renovations<br>
    Bathroom and kitchen renovations<br>
    House extensions<span class="sep">|</span>New builds and granny flats
  </p>
</section>

</body>
</html>
```